Australian residential property business needs a business card design

I need a business card design for my new business 'Harbour Estate Ventures'. The business will involve house purchases, land development sites, renovation projects, sub-divisions etc. I will be buying property from motivated vendors and working with property investors. I will deal with a wide range of people working in the residential property market including real estate agents, councils, tradespeople, banks, home owners, etc.

I would like something simple, not flashy, but a little bit unique. The colours should be in line with my logo. The business card needs to be professional. I would like something memorable, but not 'busy' or too bright. Not boring. Modern ok.

Target Market(s)

Home owners looking to sell their property, real estate agents, tradespeople (e.g. plumbers, builders, electricians etc), property investors, local councils, and anyone else involved in the residential property industry

Industry/Entity Type

Business

Contact Information for Business Card

I need to include my business name/logo, my name, my title, a PO Box number/address, a mobile number, and an email address.

Font styles to use
Serif

Requirements
Must have
• My business card details listed above.

```html
<!DOCTYPE html>
<html lang="en">
<head>
<meta charset="UTF-8">
<title>Harbour Estate Ventures – Business Card</title>
<link rel="stylesheet" href="https://fonts.googleapis.com/css2?family=Lato:wght@400;700;900&display=swap">
<style>
  :root {
    --backdrop: #e4e4e4;
    --card: #111419;
    --card-sheen: #1c2026;
    --green: #1fa64a;
    --amber: #f2a81d;
    --silver: #c9c9c9;
    --white: #f4f4f4;
    --divider: #4a4e55;
  }
  * { margin: 0; padding: 0; box-sizing: border-box; }
  html, body {
    width: 1200px; height: 900px; overflow: hidden;
    background: var(--backdrop);
    font-family: "Lato", sans-serif;
  }
  .stage { position: relative; width: 1200px; height: 900px; }

  .card {
    position: absolute;
    left: 320px;
    width: 560px; height: 320px;
    background: linear-gradient(100deg, var(--card) 60%, var(--card-sheen) 100%);
    box-shadow: 0 4px 12px rgba(0,0,0,.2);
    overflow: hidden;
  }
  .card--back { top: 110px; }
  .card--front { top: 470px; }

  .wordmark {
    display: flex; align-items: center; gap: 10px;
    font-weight: 900; letter-spacing: .5px;
    text-transform: uppercase; white-space: nowrap;
  }
  .wordmark__mark { width: 14px; height: 14px; flex: none; }
  .wordmark__text { display: block; line-height: 1.15; }

  .card--back .wordmark {
    position: absolute; left: 50%; top: 50%;
    transform: translate(-50%, -50%);
    color: var(--silver); font-size: 22px;
  }
  .card--back .wordmark__mark { background: var(--silver); }

  .tab {
    position: absolute; height: 12px; width: 160px;
    background: var(--green); border-radius: 8px;
  }
  .tab--top { top: -6px; left: 120px; }
  .tab--bottom { bottom: -6px; left: 210px; }

  .card--front .wordmark {
    position: absolute; left: 36px; top: 140px;
    color: var(--amber); font-size: 19px;
  }
  .card--front .wordmark__mark { background: var(--amber); }

  .divider {
    position: absolute; left: 250px; top: 95px;
    width: 1px; height: 130px; background: var(--divider);
  }

  .contact {
    position: absolute; left: 290px; top: 84px;
    color: var(--white);
  }
  .contact__name { font-weight: 700; font-size: 17px; letter-spacing: .5px; text-transform: uppercase; }
  .contact__title { color: var(--green); font-size: 13px; letter-spacing: .5px; text-transform: uppercase; margin-bottom: 12px; }
  .contact__line { display: flex; align-items: center; gap: 8px; font-size: 13.5px; line-height: 20px; }
  .contact__line svg { width: 11px; height: 11px; fill: var(--green); flex: none; }
  .contact__address { font-size: 13.5px; line-height: 17px; margin-top: 10px; padding-left: 19px; }
</style>
</head>
<body>
<main class="stage">
  <section class="card card--back" aria-label="Card back">
    <div class="wordmark"><span class="wordmark__mark"></span><span class="wordmark__text">Harbour Estate Ventures</span></div>
  </section>

  <section class="card card--front" aria-label="Card front">
    <span class="tab tab--top"></span>
    <span class="tab tab--bottom"></span>
    <div class="wordmark">
      <span class="wordmark__mark"></span>
      <span class="wordmark__text">Harbour Estate<br>Ventures</span>
    </div>
    <span class="divider"></span>
    <div class="contact">
      <p class="contact__name">Marcus Hale</p>
      <p class="contact__title">Managing Director</p>
      <p class="contact__line">
        <svg viewBox="0 0 24 24" aria-hidden="true"><path d="M6.6 10.8a15.1 15.1 0 0 0 6.6 6.6l2.2-2.2a1 1 0 0 1 1-.25 11.4 11.4 0 0 0 3.6.57 1 1 0 0 1 1 1V20a1 1 0 0 1-1 1A17 17 0 0 1 3 4a1 1 0 0 1 1-1h3.5a1 1 0 0 1 1 1c0 1.25.2 2.45.57 3.6a1 1 0 0 1-.25 1z"/></svg>
        0000-987-654
      </p>
      <p class="contact__line">
        <svg viewBox="0 0 24 24" aria-hidden="true"><path d="M2 5h20v14H2z"/></svg>
        hello@harbourestate.com
      </p>
      <p class="contact__address">1820 Kensington Lane<br>Portland, OR 97205</p>
    </div>
  </section>
</main>
</body>
</html>
```